Require stationery design which includes the following items as a minimum.

- Business card design
- Letterhead
- Envelopes

Details for business card:
Logo: Main logo is called "dove interiors square gold" but you may make use of whichever logo works best.
Tagline: Exquisite Furniture & Furnishings
Name: Helen Marchetti
Title: Interior Stylist
Mobile: 0432 871 264
PH: 03 9572 3140
Email: helen@dove-interiors.com.au

```html
<!DOCTYPE html>
<html lang="en">
<head>
<meta charset="utf-8">
<title>Dove Interiors – Business Card</title>
<link rel="stylesheet" href="https://fonts.googleapis.com/css2?family=Crimson+Text:wght@400;600&family=Open+Sans:wght@400;600&display=swap">
<style>
  :root {
    --backdrop: #3a302b;
    --card: #141414;
    --card-edge: #0a0a0a;
    --stack: #0d0d0d;
    --gold: #c9a24a;
    --gold-light: #e6c77a;
    --text-light: #f2f2f2;
    --serif: "Crimson Text", Georgia, serif;
    --sans: "Open Sans", Arial, sans-serif;
  }
  * { box-sizing: border-box; margin: 0; padding: 0; }
  html, body { width: 1200px; height: 716px; overflow: hidden; }
  body {
    background: var(--backdrop);
    position: relative;
    font-family: var(--sans);
  }

  .card {
    position: absolute;
    top: 196px;
    width: 540px;
    height: 316px;
    background: var(--card);
    border: 1px solid var(--card-edge);
    box-shadow: 0 12px 30px rgba(0,0,0,.5);
  }
  .card--front {
    left: 40px;
    box-shadow: 0 3px 0 var(--stack), 0 6px 0 var(--card-edge), 0 9px 0 var(--stack), 0 18px 30px rgba(0,0,0,.5);
  }
  .card--back { left: 620px; }

  /* Brand name set in the serif, one colour, one weight */
  .brand {
    position: absolute;
    left: 0; right: 0;
    display: flex;
    justify-content: center;
    align-items: center;
    gap: 16px;
    color: var(--gold);
    font-family: var(--serif);
    font-weight: 600;
    text-transform: uppercase;
    line-height: 1;
  }
  .brand__square {
    width: 34px; height: 34px;
    border: 2px solid var(--gold);
    flex: none;
  }
  .brand__words { display: flex; flex-direction: column; align-items: center; }
  .brand__main { font-size: 54px; letter-spacing: 5px; }
  .brand__sub { font-size: 16px; letter-spacing: 7px; margin-top: 4px; }

  .card--front .brand { top: 88px; }
  .card--back .brand { top: 40px; }

  .rule {
    position: absolute;
    left: 50%;
    transform: translateX(-50%);
    height: 1px;
    background: linear-gradient(90deg, transparent, var(--gold-light), transparent);
  }
  .card--front .rule { width: 330px; top: 192px; }
  .tagline {
    position: absolute;
    left: 0; right: 0; top: 204px;
    text-align: center;
    color: var(--gold);
    font-family: var(--serif);
    font-size: 17px;
  }

  .person {
    position: absolute;
    left: 0; right: 0; top: 144px;
    text-align: center;
  }
  .person__name {
    color: var(--gold);
    font-weight: 600;
    font-size: 20px;
    line-height: 1.2;
  }
  .person__title {
    margin-top: 2px;
    color: var(--text-light);
    font-size: 13px;
  }
  .card--back .rule { width: 200px; top: 196px; }

  .contacts {
    position: absolute;
    left: 40px; right: 40px; top: 228px;
    display: grid;
    grid-template-columns: 1fr auto;
    row-gap: 14px;
    font-size: 14px;
    color: var(--text-light);
  }
  .contacts__email { grid-column: 1 / -1; }
  .contacts__label { color: var(--gold); font-weight: 600; margin-right: 4px; }
</style>
</head>
<body>
  <section class="card card--front">
    <div class="brand">
      <span class="brand__square"></span>
      <span class="brand__words"><span class="brand__main">Dove</span><span class="brand__sub">Interiors</span></span>
    </div>
    <span class="rule"></span>
    <p class="tagline">Exquisite Furniture &amp; Furnishings</p>
  </section>

  <section class="card card--back">
    <div class="brand">
      <span class="brand__square"></span>
      <span class="brand__words"><span class="brand__main">Dove</span><span class="brand__sub">Interiors</span></span>
    </div>
    <div class="person">
      <p class="person__name">Helen Marchetti</p>
      <p class="person__title">Interior Stylist</p>
    </div>
    <span class="rule"></span>
    <div class="contacts">
      <p><span class="contacts__label">Mobile:</span>0432 871 264</p>
      <p><span class="contacts__label">Phone:</span>03 9572 3140</p>
      <p class="contacts__email"><span class="contacts__label">Email:</span>helen@dove-interiors.com.au</p>
    </div>
  </section>
</body>
</html>
```